Oil Field Service company needs professional business cards

Looking to clean up our current company business cards and look a little more professional. Harlow Tubular Services is a US based company that services the oil field. We deal with engineers, managers and oil rigs....................................................................................................................................................................................................................................................................................................................................................................................................

Target Market(s)

Oil and Gas professionals

Industry/Entity Type

Oil And Gas

Contact Information for Business Card

See attached photo as example

Font styles to use
Sans Serif

Colors
ec1f27

Requirements
Must have
• Company Logo, Name, Title, Cell, Office, Fax, Email.
• See attached photo
Nice to have
• External CRT, Internal CRT, Casing Crews, Torque Turn, Laydown Machine
Should not have
• Do not introduce any new pictures and keep it professional looking

```html
<!DOCTYPE html>
<html lang="en">
<head>
<meta charset="utf-8">
<title>Harlow Tubular Services – Business Card</title>
<link rel="stylesheet" href="https://fonts.googleapis.com/css2?family=Open+Sans:wght@400;600;700;800&family=Fira+Sans+Condensed:wght@600&display=swap">
<style>
  :root {
    --backdrop: #2e2f31;
    --slate: #3e4a55;
    --red: #e31b23;
    --paper: #f7f7f7;
    --ink: #2f3a44;
    --light: #eef1f3;
  }
  * { margin: 0; padding: 0; box-sizing: border-box; }
  html, body { width: 1200px; height: 750px; overflow: hidden; background: var(--backdrop); }
  body { position: relative; font-family: "Open Sans", Arial, sans-serif; }

  .card {
    position: absolute;
    top: 228px;
    width: 461px;
    height: 262px;
    overflow: hidden;
  }
  .card--front { left: 124px; background: var(--paper); }
  .card--back  { left: 618px; background: var(--slate); }

  .panel { position: absolute; inset: 0; width: 100%; height: 100%; }

  .brand { position: absolute; text-align: center; font-weight: 800; line-height: 1; }
  .brand__main { display: block; font-size: 34px; letter-spacing: 1px; }
  .brand__sub  { display: block; font-size: 11px; letter-spacing: 3px; margin-top: 9px; }
  .card--front .brand { left: 34px; top: 40px; width: 192px; color: var(--ink); }
  .card--back  .brand { left: 52px; top: 117px; width: 190px; color: var(--paper); }

  .person { position: absolute; left: 34px; top: 136px; }
  .person__name {
    font-family: "Fira Sans Condensed", "Arial Narrow", sans-serif;
    font-weight: 600; font-size: 19px; color: var(--red); line-height: 1;
  }
  .person__title { font-size: 12.5px; font-weight: 600; color: var(--ink); margin-top: 5px; }

  .contact { position: absolute; right: 24px; top: 131px; list-style: none; }
  .contact li {
    display: flex; justify-content: flex-end; align-items: center;
    height: 17.6px; font-size: 12.5px; color: var(--light);
  }
  .contact .address { margin-bottom: 4px; }
  .contact .mobile { font-weight: 700; }
  .contact svg { width: 11px; height: 11px; margin-left: 8px; fill: var(--red); flex: none; }

  .divider {
    position: absolute; left: 259px; top: 92px; width: 1px; height: 100px;
    background: rgba(255,255,255,0.35);
  }
  .services { position: absolute; left: 284px; top: 93px; list-style: none; }
  .services li {
    position: relative; padding-left: 10px; height: 19.3px;
    font-size: 13px; color: var(--light); line-height: 19px;
  }
  .services li::before {
    content: ""; position: absolute; left: 0; top: 8px;
    width: 4px; height: 4px; border-radius: 50%; background: var(--red);
  }
</style>
</head>
<body>

  <section class="card card--front">
    <svg class="panel" viewBox="0 0 461 262" aria-hidden="true">
      <polygon points="0,240 461,36 461,262 0,262" fill="var(--slate)"/>
      <line x1="0" y1="240" x2="461" y2="36" stroke="var(--red)" stroke-width="3"/>
    </svg>

    <div class="brand">
      <span class="brand__main">HARLOW</span>
      <span class="brand__sub">TUBULAR SERVICES</span>
    </div>

    <div class="person">
      <div class="person__name">COLE BRANNIGAN</div>
      <div class="person__title">AREA MANAGER</div>
    </div>

    <ul class="contact">
      <li class="address">Harmon, OK 73832</li>
      <li>(555)014-2200
        <svg viewBox="0 0 24 24"><path d="M6.6 10.8a15.1 15.1 0 0 0 6.6 6.6l2.2-2.2c.3-.3.7-.4 1-.2 1.1.4 2.3.6 3.6.6.6 0 1 .4 1 1V20c0 .6-.4 1-1 1A17 17 0 0 1 3 4c0-.6.4-1 1-1h3.5c.6 0 1 .4 1 1 0 1.3.2 2.5.6 3.6.1.3 0 .7-.2 1z"/></svg>
      </li>
      <li class="mobile">(555)017-3381
        <svg viewBox="0 0 24 24"><path d="M7 1h10a2 2 0 0 1 2 2v18a2 2 0 0 1-2 2H7a2 2 0 0 1-2-2V3a2 2 0 0 1 2-2zm0 3v15h10V4z"/></svg>
      </li>
      <li>(555)014-2291
        <svg viewBox="0 0 24 24"><path d="M6 2h9l3 3v5H6zM3 11h18a2 2 0 0 1 2 2v7H1v-7a2 2 0 0 1 2-2zm3 4v2h4v-2z"/></svg>
      </li>
      <li>cole@harlowtubular.com
        <svg viewBox="0 0 24 24"><path d="M2 5h20v14H2zm2 2v.5l8 5.5 8-5.5V7z"/></svg>
      </li>
      <li>www.harlowtubular.com
        <svg viewBox="0 0 24 24"><path d="M12 2a10 10 0 1 0 0 20 10 10 0 0 0 0-20zm0 2.2c1.2 1.3 2 3.2 2.3 5.3H9.7c.3-2.1 1.1-4 2.3-5.3zM4.3 11.5h3.3c.1 2.3.7 4.4 1.8 6A7.8 7.8 0 0 1 4.3 11.5zm5.4 0h4.6c-.1 2.4-.9 4.6-2.3 6-1.4-1.4-2.200-3.6-2.3-6zm6.7 0h3.3a7.8 7.8 0 0 1-5.1 6c1.1-1.6 1.7-3.7 1.8-6z"/></svg>
      </li>
    </ul>
  </section>

  <section class="card card--back">
    <div class="brand">
      <span class="brand__main">HARLOW</span>
      <span class="brand__sub">TUBULAR SERVICES</span>
    </div>

    <div class="divider"></div>

    <ul class="services">
      <li>External CRT</li>
      <li>Internal CRT</li>
      <li>Casing Crews</li>
      <li>Torque Turn</li>
      <li>Laydown Machine</li>
    </ul>
  </section>

</body>
</html>
```